Business card for Property Management consultant

I need a business card for my business LX Vantage - I consult to real estate agents to improve the performance of their Property Management departments (rental houses management). The card needs to be very professional looking, incorporating our logo and my photo plus the line "Develop your Rent Roll to Perform"

Target Market(s)

Real Estate business owners

Industry/Entity Type

Business Consultant

Contact Information for Business Card

Business name - LX Vantage (logo uploaded)
My Name : Marcia Kellaway -
Title : Property Management Consultant

Develop your Rent Roll to perform

Phone : +61 438592716
email : marcia@lxvantage.com.au
website ; www.lxvantage.com.au

Requirements
Must have
• Logo
• My photo
• Very corporate / professional look

```html
<!DOCTYPE html>
<html lang="en">
<head>
<meta charset="utf-8">
<title>LX Vantage — Business Card</title>
<link rel="stylesheet" href="https://fonts.googleapis.com/css2?family=Montserrat:wght@400;500;600&family=Roboto+Condensed:wght@400&display=swap">
<style>
  :root {
    --page-bg: #1a1a1c;
    --card-bg: #ffffff;
    --ink-dark: #1d1d22;
    --navy: #2a3a78;
    --royal: #3e6fc2;
    --gold: #c8901f;
    --grey-text: #3a3a3a;
    --photo-light: #eceef2;
    --photo-warm: #a5654a;
    --photo-jacket: #2f62c4;
  }
  * { margin: 0; padding: 0; box-sizing: border-box; }
  html, body {
    width: 1200px; height: 1120px; overflow: hidden;
    background: var(--page-bg);
  }
  .canvas {
    position: relative; width: 1200px; height: 1120px;
    display: flex; align-items: center; justify-content: center;
  }
  .business-card {
    position: relative; width: 1000px; height: 560px;
    background: var(--card-bg);
    overflow: hidden;
    box-shadow: 0 20px 50px rgba(0,0,0,.5);
  }
  .portrait {
    position: absolute; left: 0; bottom: 0;
    width: 470px; height: 500px;
    background: linear-gradient(to bottom,
      var(--card-bg) 0%,
      var(--photo-light) 25%,
      #d9b4a2 50%,
      var(--photo-light) 66%,
      var(--photo-jacket) 80%,
      var(--photo-jacket) 100%);
  }
  .accent-band {
    position: absolute; right: 0; bottom: 0;
    width: 530px; height: 12px;
    background: var(--royal);
  }
  .info-block {
    position: absolute; right: 56px; top: 48px;
    width: 420px;
    font-family: "Montserrat", sans-serif;
  }
  .brand {
    display: flex; align-items: center; gap: 14px;
  }
  .brand-square {
    width: 44px; height: 44px; background: var(--royal);
  }
  .brand-name {
    font-family: "Montserrat", sans-serif;
    font-weight: 600; font-size: 50px; letter-spacing: 1px;
    color: var(--ink-dark); line-height: 1;
  }
  .role-title {
    margin-top: 26px;
    font-weight: 500; font-size: 17px; letter-spacing: 1px;
    color: var(--navy);
  }
  .person-name {
    margin-top: 30px;
    font-family: "Roboto Condensed", sans-serif;
    font-weight: 400; font-size: 40px; color: var(--gold); line-height: 1;
  }
  .promise-line {
    margin-top: 6px;
    font-size: 15px; letter-spacing: 1px; color: var(--royal);
  }
  .contact-list {
    position: absolute; left: 560px; bottom: 60px;
    font-family: "Montserrat", sans-serif;
    list-style: none; text-align: left;
  }
  .contact-phone {
    font-weight: 600; font-size: 24px; color: var(--navy); letter-spacing: 1px;
  }
  .contact-line {
    font-size: 17px; color: var(--grey-text); letter-spacing: 1px; line-height: 1.35;
  }
</style>
</head>
<body>
  <main class="canvas">
    <article class="business-card">
      <div class="portrait" role="img" aria-label="Portrait photo of Marcia Kellaway in a blue jacket"></div>
      <div class="accent-band"></div>

      <section class="info-block">
        <div class="brand">
          <span class="brand-square"></span>
          <span class="brand-name">LX Vantage</span>
        </div>
        <p class="role-title">Property Management Consultant</p>
        <h1 class="person-name">Marcia Kellaway</h1>
        <p class="promise-line">Develop Your Rent Roll to perform</p>
      </section>

      <ul class="contact-list">
        <li class="contact-phone">+61 438592716</li>
        <li class="contact-line">marcia@lxvantage.com.au</li>
        <li class="contact-line">www.lxvantage.com.au</li>
      </ul>
    </article>
  </main>
</body>
</html>
```